Amber Ridge Publishing Web Page Design

Design a website for my new start up publishing company - Amber Ridge Publishing, the first work published by ARP with be a new book by M.R. Theodor called Silent Ledger. The prototype for the book cover is attached.

Target Market(s)

Worldwide, all readers of mystery, fiction, etc.

Industry/Entity Type

Book Publisher

Coding

Coded - Design and coding required

Number of Pages Required

1 page

```html
<!DOCTYPE html>
<html lang="en">
<head>
<meta charset="utf-8">
<title>Amber Ridge Publishing</title>
<link rel="stylesheet" href="https://fonts.googleapis.com/css2?family=Montserrat:wght@600;700&family=Arimo:wght@400;700&family=Open+Sans:wght@400;700&display=swap">
<style>
:root{
  --page:#ecebe8;
  --header:#e8e8e8;
  --navy:#1b4a78;
  --blue-deep:#163f6a;
  --blue-mid:#1f5f98;
  --green:#6aa51a;
  --green-dark:#4f8410;
  --green-light:#82bf22;
  --yellow:#ffc80d;
  --text:#4a4a4a;
  --muted:#777;
  --line:#b5b5b5;
  --red:#e0534d;
  --teal:#5f9a93;
  --slate:#8c9699;
}
*{margin:0;padding:0;box-sizing:border-box}
html,body{width:927px;height:1200px;overflow:hidden}
body{background:var(--page);font-family:"Arimo",Arial,sans-serif;color:var(--text);position:relative}
.abs{position:absolute}

.site-header{left:0;top:0;width:927px;height:98px;background:var(--header)}
.brand{left:168px;top:44px;display:flex;align-items:center;gap:10px}
.brand-mark{width:30px;height:30px;background:var(--green)}
.brand-name{font-family:"Montserrat",sans-serif;font-weight:700;font-size:17px;color:#5a5a5a;letter-spacing:1px}
.main-nav{left:488px;top:74px;display:flex;gap:16px;font-size:10.5px;color:#3d3d3d}
.main-nav .active{color:#2f7db7}

.hero{left:0;top:98px;width:927px;height:252px;background:radial-gradient(ellipse at 65% 45%,#2a72b2 0%,var(--blue-mid) 35%,var(--blue-deep) 100%)}
.hero-arrow{width:38px;height:38px;border-radius:50%;background:#fff;border:3px solid #173a60;top:67px;box-shadow:0 2px 4px rgba(0,0,0,.4)}
.hero-arrow svg{display:block;margin:8px auto}
.hero-title{left:208px;font-family:"Montserrat",sans-serif;font-weight:700;color:#fff;line-height:1}
.t1{top:26px;font-size:25px}
.t2{top:61px;font-size:25px}
.t3{top:92px;font-size:25px}
.t4{top:123px;font-size:25px;color:var(--yellow)}
.t5{top:162px;font-size:14px}
.btn-purchase{left:208px;top:207px;width:94px;height:23px;border-radius:6px;background:linear-gradient(#82c126,#4e8a0f);border:1px solid #9fd84a;color:#fff;font-family:"Montserrat",sans-serif;font-weight:700;font-size:10px;letter-spacing:1px;display:flex;align-items:center;justify-content:center}
.hero-cover{left:540px;top:10px;width:150px;height:238px;background:linear-gradient(160deg,#1c2a6a,#2c3f8f 55%,#1b2454);box-shadow:6px 4px 10px rgba(0,0,0,.45);border-right:6px solid #e8e8e8}

.info h3{font-size:10.5px;font-weight:700;color:var(--navy);margin-bottom:10px}
.info p{font-size:7.4px;line-height:13.9px;color:#555}
.col-about{left:169px;top:379px;width:150px}
.col-services{left:372px;top:376px;width:158px}
.col-contact{left:586px;top:376px;width:200px}
.divider{top:379px;width:1px;height:126px;background:#888}
.contact-row{display:flex;align-items:center;gap:8px;font-size:10px;color:#555;margin-bottom:8px}
.connect{font-size:11px;color:var(--green);margin:26px 0 9px}
.socials{display:flex;gap:10px}
.socials span{width:19px;height:19px;border-radius:3px}
.s1{background:#5bbce4}.s2{background:#3b5b9a}.s3{background:#1e7ab8}

.section-title{left:168px;top:546px;font-family:"Montserrat",sans-serif;font-weight:600;font-size:20px;color:var(--navy)}
.section-rule{left:386px;top:558px;width:374px;height:2px;background:#b9b9b9}

.card{width:137px;height:192px;background:#fff;box-shadow:0 0 3px rgba(0,0,0,.08)}
.card .cover{position:absolute;left:31px;top:10px;width:68px;height:110px;background:linear-gradient(160deg,#1c2a6a,#2d3f8e 55%,#1b2454);border-right:3px solid #ddd;box-shadow:3px 2px 4px rgba(0,0,0,.35)}
.card p{position:absolute;left:6px;right:6px;top:136px;font-family:"Open Sans",sans-serif;font-size:6.6px;line-height:10px;color:#666;text-align:center}
.btn-read{position:absolute;left:19px;top:180px;width:102px;height:27px;background:var(--green-light);border-bottom:3px solid var(--green-dark);color:#fff;font-family:"Open Sans",sans-serif;font-weight:700;font-size:7.5px;display:flex;align-items:center;justify-content:center}

.pager{top:1054px;width:23px;height:23px;border-radius:2px;background:var(--slate);color:#fff;font-family:"Open Sans",sans-serif;font-weight:700;font-size:9px;display:flex;align-items:center;justify-content:center}
.pager.current{background:var(--teal)}
.pager.hot{background:var(--red)}

.site-footer{left:0;top:1093px;width:927px;height:107px;background:linear-gradient(#11508d,var(--blue-deep))}
.login{top:25px;height:16px;width:83px;background:#fff;border-radius:2px;font-family:"Open Sans",sans-serif;font-weight:700;font-size:6.5px;letter-spacing:.5px;color:#333;display:flex;align-items:center;gap:3px;padding-left:4px}
.legal{right:207px;top:29px;font-family:"Open Sans",sans-serif;font-weight:700;font-size:6.8px;color:#fff;letter-spacing:.4px}
.footer-rule{left:204px;top:49px;width:520px;height:1px;background:#4f7aa6}
.footer-nav{left:0;width:927px;top:64px;text-align:center;font-family:"Open Sans",sans-serif;font-weight:700;font-size:7px;color:#fff;word-spacing:2px}
.copyright{left:0;width:927px;top:81px;text-align:center;font-family:"Open Sans",sans-serif;font-size:6.5px;color:#cfd9e5;letter-spacing:.3px}
</style>
</head>
<body>

<header class="site-header abs">
  <div class="brand abs"><span class="brand-mark"></span><span class="brand-name">AMBER RIDGE PUBLISHING</span></div>
  <nav class="main-nav abs"><span class="active">HOME</span><span>ABOUT</span><span>SERVICES</span><span>BOOKS</span><span>CONTACT</span></nav>
</header>

<section class="hero abs">
  <div class="hero-arrow abs" style="left:149px"><svg width="16" height="16" viewBox="0 0 16 16"><path d="M11 2 5 8l6 6" fill="none" stroke="#5c9a14" stroke-width="3.5"/></svg></div>
  <div class="hero-arrow abs" style="left:742px"><svg width="16" height="16" viewBox="0 0 16 16"><path d="M5 2l6 6-6 6" fill="none" stroke="#5c9a14" stroke-width="3.5"/></svg></div>
  <div class="hero-title abs t1">NEW BOOK BY</div>
  <div class="hero-title abs t2">M.R. THEODOR</div>
  <div class="hero-title abs t3">CALLED</div>
  <div class="hero-title abs t4">SILENT LEDGER</div>
  <div class="hero-title abs t5">PUBLISHED BY ARP</div>
  <div class="btn-purchase abs">PURCHASE</div>
  <div class="hero-cover abs" role="img" aria-label="Book cover of Silent Ledger by M.R. Theodor"></div>
</section>

<section class="info">
  <div class="col-about abs">
    <h3>ABOUT ME</h3>
    <p>Lorem ipsum dolor sit amet, consectetur adipiscing elit. Aenean placerat porttitor ligula quis fringilla. Vestibulum viverra justo in dui pellentesque convallis. Vivamus ac ligula felis, et bibendum urna. Mauris vitae mauris quis arcu rhoncus auctor ac eu nibh. Vestibulum volutpat justo sit amet nisi auctor vitae rutrum dui porttitor.</p>
  </div>
  <div class="divider abs" style="left:343px"></div>
  <div class="col-services abs">
    <h3>MY SERVICES</h3>
    <p>Lorem ipsum dolor sit amet, consectetur adipiscing elit. Aenean placerat porttitor ligula quis fringilla. Vestibulum viverra justo in dui pellentesque convallis. Vivamus ac ligula felis, et bibendum urna. Mauris vitae mauris quis arcu rhoncus auctor ac eu nibh. Vestibulum volutpat justo sit amet nisi auctor vitae rutrum dui porttitor.</p>
  </div>
  <div class="divider abs" style="left:556px"></div>
  <div class="col-contact abs">
    <h3>CONTACT US</h3>
    <div class="contact-row"><svg width="12" height="9" viewBox="0 0 12 9"><rect width="12" height="9" fill="#6aa51a"/><path d="M0 0l6 5 6-5" fill="none" stroke="#fff" stroke-width="1.2"/></svg>info@amberridgepublishing.com</div>
    <div class="contact-row"><svg width="12" height="12" viewBox="0 0 12 12"><path d="M3 1 5 4 4 5c.8 1.5 1.5 2.2 3 3l1-1 3 2-1 2C5 11 1 7 1 2z" fill="#6aa51a"/></svg>555-014-2290</div>
    <div class="connect">CONNECT WITH ME</div>
    <div class="socials"><span class="s1"></span><span class="s2"></span><span class="s3"></span></div>
  </div>
</section>

<h2 class="section-title abs">NEW BOOK ARRIVAL</h2>
<div class="section-rule abs"></div>

<div class="card abs" style="left:168px;top:590px"><div class="cover" role="img" aria-label="Book cover"></div><p>Quisque id tellus quis risus vehicula vehicula ut turpis. In eros nulla, placerat vitae at, vehicula ut nunc.</p><div class="btn-read">read more</div></div>
<div class="card abs" style="left:320px;top:590px"><div class="cover" role="img" aria-label="Book cover"></div><p>Ut eleifend libero sed neque rhoncus consequat. Maecenas tincidunt, augue et rutrum condimentum, libero lectus.</p><div class="btn-read">read more</div></div>
<div class="card abs" style="left:473px;top:590px"><div class="cover" role="img" aria-label="Book cover"></div><p>Vivamus eget ante bibendum arcu vehicula ultricies. Integer venenatis mattis nisl, vitae pulvinar dui tempor .</p><div class="btn-read">read more</div></div>
<div class="card abs" style="left:625px;top:590px"><div class="cover" role="img" aria-label="Book cover"></div><p>Astehicula ultricies. Integer venenatis mattis nisl, vitae pulvinar dui tempor non.</p><div class="btn-read">read more</div></div>

<div class="card abs" style="left:168px;top:826px"><div class="cover" role="img" aria-label="Book cover"></div><p>Quisque id tellus quis risus vehicula vehicula ut turpis. In eros nulla, placerat vitae at, vehicula ut nunc.</p><div class="btn-read">read more</div></div>
<div class="card abs" style="left:320px;top:826px"><div class="cover" role="img" aria-label="Book cover"></div><p>Ut eleifend libero sed neque rhoncus consequat. Maecenas tincidunt, augue et rutrum condimentum, libero lectus.</p><div class="btn-read">read more</div></div>
<div class="card abs" style="left:473px;top:826px"><div class="cover" role="img" aria-label="Book cover"></div><p>Vivamus eget ante bibendum arcu vehicula ultricies. Integer venenatis mattis nisl, vitae pulvinar dui tempor .</p><div class="btn-read">read more</div></div>
<div class="card abs" style="left:625px;top:826px"><div class="cover" role="img" aria-label="Book cover"></div><p>Astehicula ultricies. Integer venenatis mattis nisl, vitae pulvinar dui tempor non.</p><div class="btn-read">read more</div></div>

<nav class="pagination">
  <div class="pager abs" style="left:299px"><svg width="8" height="8" viewBox="0 0 8 8"><path d="M6 0 2 4l4 4" fill="none" stroke="#fff" stroke-width="2"/></svg></div>
  <div class="pager abs" style="left:340px">1</div>
  <div class="pager current abs" style="left:369px">2</div>
  <div class="pager abs" style="left:398px">3</div>
  <div class="pager abs" style="left:426px">4</div>
  <div class="pager abs" style="left:455px">5</div>
  <div class="pager abs" style="left:485px">...</div>
  <div class="pager abs" style="left:514px">10</div>
  <div class="pager hot abs" style="left:542px">11</div>
  <div class="pager abs" style="left:571px">12</div>
  <div class="pager abs" style="left:606px"><svg width="8" height="8" viewBox="0 0 8 8"><path d="M2 0l4 4-4 4" fill="none" stroke="#fff" stroke-width="2"/></svg></div>
</nav>

<footer class="site-footer abs">
  <div class="login abs" style="left:204px"><svg width="8" height="9" viewBox="0 0 8 9"><path d="M4 0 8 1.5V4c0 2.5-2 4-4 5C2 8 0 6.5 0 4V1.5z" fill="#4caf2a"/><path d="M2 4.5l1.5 1.5L6 3" fill="none" stroke="#fff" stroke-width="1"/></svg>CLIENT LOGIN</div>
  <div class="login abs" style="left:293px"><svg width="8" height="9" viewBox="0 0 8 9"><path d="M4 0 8 1.5V4c0 2.5-2 4-4 5C2 8 0 6.5 0 4V1.5z" fill="#4caf2a"/><path d="M2 4.5l1.5 1.5L6 3" fill="none" stroke="#fff" stroke-width="1"/></svg>MEMBER LOGIN</div>
  <div class="legal abs">Terms of Services | Privacy Policy</div>
  <div class="footer-rule abs"></div>
  <div class="footer-nav abs">HOME &nbsp;&nbsp;|&nbsp;&nbsp; HOME &nbsp;&nbsp;|&nbsp;&nbsp; ABOUT &nbsp;&nbsp;|&nbsp;&nbsp; SERVICES &nbsp;&nbsp;|&nbsp;&nbsp; BOOKS &nbsp;&nbsp;|&nbsp;&nbsp; CONTACT</div>
  <div class="copyright abs">Copyright 2019. All Rights Reserved. Amber Ridge Publishing</div>
</footer>

</body>
</html>
```